Illustrate a statistic and its significance

Please create a graphical representation of the success rate of the Vail Procedure for our website. The Vail Procedure has a success rate of 80%. This means the procedure is successful for 8 out of every 10 people. An 80% success rate by itself is great. However, it's even more impressive when you consider that the only people we perform this procedure on are patients who have exhausted conventional treatment options for migraines and headaches. I would really like to emphasize both the success rate and the type of patients we are successful in treating with this procedure.
For example, you could create an illustration of outlines of 10 people with 8 of them shaded in, which would represent an 80% success rate. Then, underneath this image, you could add a bullet list of the types of treatments patients (such as the 10 figures in the image) have tried before coming to us/having this procedure, which include the following:
Prescription medications
Trigger point injections
Nerve blocks
Migraine surgery
Dermil
Chiropractic care
Physical therapy
Biofeedback
Massage
Acupuncture
Or maybe there is another/better way to represent this statistic graphically? I'm just looking for an effective illustration of this important statistic and its significance.
Our brand colors are red (#fd444a) and blue (#214170)
Thank you!
People who suffer from chronic migraines and headaches
Healthcare/Medical
- Athiti

```html
<!DOCTYPE html>
<html lang="en">
<head>
<meta charset="utf-8">
<title>Vail Procedure Success Rate</title>
<link href="https://fonts.googleapis.com/css2?family=Arimo:wght@400;700&display=swap" rel="stylesheet">
<style>
  :root {
    --bg-deep: #050d3a;
    --bg-mid: #0b2a8a;
    --bg-glow: #2a7be0;
    --title-band-a: #1c6fb8;
    --title-band-b: #0e4a8c;
    --panel: rgba(20, 90, 190, 0.72);
    --head-lit-a: #3d8fe8;
    --head-lit-b: #12306e;
    --head-dim: rgba(180, 200, 230, 0.28);
    --text: #ffffff;
    --glow: #7fd8ff;
  }
  * { margin: 0; padding: 0; box-sizing: border-box; }
  html, body { width: 1200px; height: 598px; overflow: hidden; background: var(--bg-deep); }
  .canvas {
    position: relative;
    width: 1200px;
    height: 598px;
    overflow: hidden;
    font-family: "Arimo", Arial, sans-serif;
    color: var(--text);
    background:
      radial-gradient(ellipse 420px 320px at 1010px 300px, rgba(60, 150, 255, 0.55), transparent 70%),
      radial-gradient(ellipse 600px 300px at 250px 120px, rgba(30, 90, 220, 0.45), transparent 70%),
      linear-gradient(160deg, var(--bg-mid) 0%, var(--bg-deep) 70%);
  }
  .backdrop-art {
    position: absolute;
    inset: 0;
    background: radial-gradient(ellipse 300px 600px at 1060px 300px, rgba(120, 200, 255, 0.25), transparent 70%);
  }
  .title-band {
    position: absolute;
    left: 27px; top: 30px;
    width: 1146px; height: 73px;
    border-radius: 10px;
    background: linear-gradient(90deg, var(--title-band-a), var(--title-band-b));
    display: flex; align-items: center; justify-content: center;
  }
  .title-band h1 {
    font-size: 41px;
    font-weight: 700;
    letter-spacing: 0.3px;
    text-shadow: 0 0 8px var(--glow), 0 0 2px var(--glow);
  }
  .patient-grid {
    position: absolute;
    left: 50px; top: 146px;
    display: grid;
    grid-template-columns: repeat(5, 140px);
    grid-template-rows: repeat(2, 150px);
    column-gap: 20px;
    row-gap: 10px;
  }
  .patient {
    border-radius: 50% 50% 40% 40%;
    background: radial-gradient(ellipse at 55% 35%, var(--head-lit-a), var(--head-lit-b) 75%);
  }
  .patient.untreated { background: var(--head-dim); }
  .treatments-panel {
    position: absolute;
    left: 878px; top: 149px;
    width: 295px; height: 334px;
    border-radius: 8px;
    background: var(--panel);
    padding: 8px 12px 0 22px;
    font-size: 19.5px;
    line-height: 20px;
  }
  .treatments-panel p { margin-bottom: 20px; }
  .treatments-panel ul { list-style: none; }
  .treatments-panel li::before { content: "· "; }
  .summary {
    position: absolute;
    left: 60px; top: 508px;
    width: 1080px;
    text-align: center;
    font-size: 18.5px;
    line-height: 21px;
    font-weight: 700;
  }
</style>
</head>
<body>
<main class="canvas">
  <div class="backdrop-art" role="img" aria-label="Glowing blue neuron network illustration"></div>

  <header class="title-band">
    <h1>The Vail Procedure has a success rate of 80%</h1>
  </header>

  <section class="patient-grid" aria-label="8 of 10 patients treated successfully">
    <div class="patient" role="img" aria-label="Head silhouette with glowing brain, successful patient"></div>
    <div class="patient" role="img" aria-label="Head silhouette with glowing brain, successful patient"></div>
    <div class="patient" role="img" aria-label="Head silhouette with glowing brain, successful patient"></div>
    <div class="patient" role="img" aria-label="Head silhouette with glowing brain, successful patient"></div>
    <div class="patient" role="img" aria-label="Head silhouette with glowing brain, successful patient"></div>
    <div class="patient" role="img" aria-label="Head silhouette with glowing brain, successful patient"></div>
    <div class="patient" role="img" aria-label="Head silhouette with glowing brain, successful patient"></div>
    <div class="patient" role="img" aria-label="Head silhouette with glowing brain, successful patient"></div>
    <div class="patient untreated" role="img" aria-label="Faded head silhouette, unsuccessful case"></div>
    <div class="patient untreated" role="img" aria-label="Faded head silhouette, unsuccessful case"></div>
  </section>

  <aside class="treatments-panel">
    <p>Types of treatments<br>these patients<br>have tried before<br>coming to us:</p>
    <ul>
      <li>Prescription medications</li>
      <li>Trigger point injections</li>
      <li>Nerve blocks</li>
      <li>Migraine surgery</li>
      <li>Dermil</li>
      <li>Chiropractic care</li>
      <li>Physical therapy</li>
      <li>Biofeedback</li>
      <li>Massage</li>
      <li>Acupuncture</li>
    </ul>
  </aside>

  <p class="summary">An 80% success rate by itself is great. However, it's even more impressive when you consider that the only people we perform this procedure on are patients who have exhausted conventional treatment options for migraines and headaches.</p>
</main>
</body>
</html>
```